Forward thinking startup needs business cards

We are a new company entering the fall protection market and we need business cards. We provide equipment and supplies to a very large industry, and we aim to catch the attention of the end-user; not just the distributors. Please browse brovatek.com for a better feel of our initial branding. The hog images are not required, but are here for inspiration. Also, they should not be prominent in the design as much as an accent. Many of our customers will be very high-end, so this should be considered as well.

Target Market(s)

Buyers for the safety industry. Some accounts will be very large, but most of these people are very down-to-earth.

Industry/Entity Type

Business

Contact Information for Business Card

Name and title
phone: 1-800-563-1804
fax: 740-555-0148
web: www.brovatek.com
address: 218 Kelbrook Lane, Dunmoor, OH 45790 USA
room for cell number, direct office phone number, extension, and email

Font styles to use
Serif
Sans Serif

Colors
f37122
ffffff

Requirements
Must have
• Should be very clean and easy to read. We typically use orange and grey in our color schemes - #ef7c2d and #424242
Nice to have
• It would be nice to have room somewhere to incorporate some of the other logos from our family of companies. At the same time, it should not look weird if they aren't included.

```html
<!DOCTYPE html>
<html lang="en">
<head>
<meta charset="utf-8">
<title>Brovatek Business Cards</title>
<link rel="stylesheet" href="https://fonts.googleapis.com/css2?family=Open+Sans:wght@400;600;800&family=Archivo+Black&display=swap">
<style>
  :root {
    --orange: #f37122;
    --orange-deep: #ef7c2d;
    --grey: #424242;
    --white: #ffffff;
    --stage: #e9e9e9;
    --ink: #1e1e1e;
  }
  * { box-sizing: border-box; margin: 0; padding: 0; }
  html, body { width: 1200px; height: 873px; overflow: hidden; }
  body {
    background: var(--stage);
    font-family: "Open Sans", Arial, sans-serif;
    color: var(--ink);
    position: relative;
  }
  .card {
    position: absolute;
    width: 434px;
    height: 242px;
    background: var(--white);
    box-shadow: 0 4px 14px rgba(0,0,0,.18);
    overflow: hidden;
  }
  /* Front */
  .card-front { left: 156px; top: 329px; }
  .front-brand {
    position: absolute; left: 14px; top: 8px; width: 406px; height: 56px;
    display: flex; align-items: center; gap: 12px;
    border-bottom: 4px solid var(--grey);
  }
  .brand-square { width: 30px; height: 30px; background: var(--grey); flex: none; }
  .brand-name {
    font-weight: 800; color: var(--orange); font-size: 48px; letter-spacing: 1px; line-height: 1;
  }
  .front-tagline {
    position: absolute; left: 0; right: 0; top: 70px; text-align: center;
    font-family: "Archivo Black", Arial, sans-serif; font-size: 23px; color: var(--grey);
    white-space: nowrap;
  }
  .front-band {
    position: absolute; left: 0; right: 0; top: 110px; height: 70px; background: var(--orange);
  }
  .mascot-art {
    position: absolute; left: 22px; top: 0; width: 400px; height: 70px;
    background: linear-gradient(90deg, #7a5a3c 0%, #a08a70 30%, #4a4a4a 50%, #6b6b6b 62%, #9a2e24 80%, #c0503a 100%);
  }
  .front-web {
    position: absolute; left: 0; right: 0; top: 184px; text-align: center;
    color: var(--orange); font-size: 36px; font-weight: 400; line-height: 54px;
  }
  .front-web .tld { font-size: 26px; }

  /* Back */
  .card-back { left: 630px; top: 326px; }
  .back-head { position: absolute; left: 0; right: 0; top: 0; height: 82px; }
  .back-brand {
    position: absolute; left: 6px; top: 6px; width: 212px; height: 28px;
    display: flex; align-items: center; gap: 6px; border-bottom: 2px solid var(--grey);
  }
  .back-brand .brand-square { width: 14px; height: 14px; }
  .back-brand .brand-name { font-size: 24px; letter-spacing: .5px; }
  .back-tagline {
    position: absolute; left: 6px; top: 38px; white-space: nowrap;
    font-family: "Archivo Black", Arial, sans-serif; font-size: 12px; color: var(--grey);
  }
  .holder-name { position: absolute; left: 6px; top: 58px; font-size: 16px; }
  .company-lines {
    position: absolute; right: 8px; top: 4px; text-align: right; font-size: 17px; line-height: 22px;
  }
  .company-lines .web { font-size: 15px; }
  .company-lines .web strong { color: var(--orange); font-weight: 400; font-size: 21px; }
  .company-lines .web .tld { font-size: 14px; }
  .back-body {
    position: absolute; left: 0; right: 0; top: 82px; height: 140px; background: var(--orange);
  }
  .holder-title { position: absolute; left: 24px; top: 8px; font-size: 16px; }
  .direct-lines { position: absolute; left: 154px; top: 8px; font-size: 16px; line-height: 20px; }
  .direct-lines li { list-style: none; margin-bottom: 20px; }
  .back-foot {
    position: absolute; left: 0; right: 0; bottom: 0; height: 20px;
    text-align: right; padding-right: 8px; font-size: 12.5px; line-height: 20px;
  }
</style>
</head>
<body>
  <section class="card card-front" aria-label="Card front">
    <div class="front-brand">
      <span class="brand-square"></span>
      <span class="brand-name">BROVATEK</span>
    </div>
    <p class="front-tagline">Secure at Every Step</p>
    <div class="front-band">
      <div class="mascot-art" role="img" aria-label="Illustration of three charging wild hog mascots"></div>
    </div>
    <p class="front-web">www.brovatek<span class="tld">.com</span></p>
  </section>

  <section class="card card-back" aria-label="Card back">
    <header class="back-head">
      <div class="back-brand">
        <span class="brand-square"></span>
        <span class="brand-name">BROVATEK</span>
      </div>
      <p class="back-tagline">Secure at Every Step</p>
      <p class="holder-name">John Doe</p>
      <div class="company-lines">
        <p>1-800-563-1804</p>
        <p>fax: 740-555-0148</p>
        <p class="web">www.<strong>brovatek</strong><span class="tld">.com</span></p>
      </div>
    </header>
    <div class="back-body">
      <p class="holder-title">Sales Rep</p>
      <ul class="direct-lines">
        <li>O: 888-888-8888 ext 888</li>
        <li>C:&nbsp; 877-777-77</li>
        <li>E: john.d@brovatek.com</li>
      </ul>
    </div>
    <footer class="back-foot">218 Kelbrook Lane, Dunmoor, OH 45790 USA</footer>
  </section>
</body>
</html>
```